Hearthside Pots: A Patient Palate's Companion

Hi, I had a book cover designed on this site, but I want to modify the cover and change the colours. I want to keep the slow cooker and the ingredients on the cover, but I want to simplify it a bit. And, I am open to other ideas. I have attached below a book cover idea I like and I like the colors as well. I want it to be called Hearthside Pots, with the language on the right corner: "Curated For Nearly Effortless Meals That Are Greater Than The Sum Of Their Ingredients" I like the circles idea and my name as the author on the curve.

Target Market(s)

Home Cooks

Colors
00AB8E
00BBA5
67D7C9
C6EFE9
E9F9F6
F0912C
F2A743
F7CA91
FBE8D2
FDF5EE
E54698
E96AAD
F1A4CE
F9D9EA
FCEFF6
6B429C
8869AF
B7A5CE
E3DAEB
F3F0F8

Requirements
Must have
• Please use the colors on the Marigold Table Recipe Book and I like the design, but I do not want it identical. I like the author name (Harold P. Quimby) on the side of the circle on the upper right side of the cover.
Nice to have
• I like the large words "Hearthside Pots"

```html
<!DOCTYPE html>
<html lang="en">
<head>
<meta charset="utf-8">
<title>Hearthside Pots — Harold P. Quimby</title>
<link rel="stylesheet" href="https://fonts.googleapis.com/css2?family=Playfair+Display:wght@900&family=Merriweather:wght@700;900&display=swap">
<style>
  :root {
    --deep-plum: #3d2360;
    --deep-teal: #00AB8E;
    --rose: #E54698;
    --marigold: #F0912C;
    --lavender: #8869AF;
    --grape: #6B429C;
    --teal: #00BBA5;
    --blush: #E96AAD;
    --paper: #ffffff;
  }
  html, body {
    margin: 0;
    padding: 0;
    overflow: hidden;
    background: var(--deep-plum);
  }
  .cover {
    position: relative;
    width: 927px;
    height: 1200px;
    overflow: hidden;
    background: var(--deep-plum);
  }
  .cover-art {
    position: absolute;
    inset: 0;
    display: block;
  }
  .author-name {
    font-family: "Merriweather", Georgia, serif;
    font-weight: 900;
    font-size: 26px;
    fill: var(--paper);
  }
  .title {
    position: absolute;
    left: 0;
    right: 0;
    top: 382px;
    margin: 0;
    text-align: center;
    font-family: "Playfair Display", "Times New Roman", serif;
    font-weight: 900;
    font-size: 128px;
    line-height: 143px;
    letter-spacing: -2px;
    color: var(--paper);
  }
  .title span { display: block; }
  .tagline {
    position: absolute;
    left: 318px;
    width: 340px;
    top: 690px;
    margin: 0;
    text-align: center;
    font-family: "Merriweather", Georgia, serif;
    font-weight: 700;
    font-size: 16.5px;
    line-height: 33px;
    color: var(--paper);
  }
</style>
</head>
<body>
<main class="cover">
  <svg class="cover-art" width="927" height="1200" viewBox="0 0 927 1200" xmlns="http://www.w3.org/2000/svg">
    <defs>
      <linearGradient id="produce-top" x1="0" y1="0" x2="1" y2="0">
        <stop offset="0" stop-color="#b8322a"/>
        <stop offset="0.45" stop-color="#c98a4a"/>
        <stop offset="0.7" stop-color="#5f9a3a"/>
        <stop offset="1" stop-color="#e8e2c4"/>
      </linearGradient>
      <radialGradient id="stew-bowl" cx="0.4" cy="0.5" r="0.6">
        <stop offset="0" stop-color="#a8321a"/>
        <stop offset="0.78" stop-color="#8a2412"/>
        <stop offset="0.82" stop-color="#f4f4f0"/>
      </radialGradient>
      <linearGradient id="cooker-spread" x1="0" y1="0" x2="1" y2="0">
        <stop offset="0" stop-color="#3f6a2a"/>
        <stop offset="0.3" stop-color="#b9a07a"/>
        <stop offset="0.5" stop-color="#b8bcbf"/>
        <stop offset="0.7" stop-color="#d24a2a"/>
        <stop offset="1" stop-color="#e8782a"/>
      </linearGradient>
      <path id="author-arc" d="M 240 184 A 176 176 0 0 1 450 274"/>
    </defs>

    <g class="backdrop">
      <rect x="0" y="0" width="927" height="1200" fill="var(--deep-plum)"/>
      <rect x="660" y="0" width="267" height="260" fill="var(--deep-teal)"/>
      <rect x="0" y="410" width="170" height="480" fill="var(--deep-teal)"/>
      <rect x="800" y="700" width="127" height="500" fill="var(--deep-teal)"/>
    </g>

    <g class="circles">
      <circle cx="172" cy="1125" r="262" fill="var(--blush)"/>
      <circle cx="720" cy="952" r="202" fill="var(--rose)"/>
      <circle cx="172" cy="720" r="210" fill="var(--marigold)"/>
      <circle cx="570" cy="285" r="180" fill="var(--lavender)"/>
      <circle cx="292" cy="352" r="218" fill="var(--rose)"/>
      <circle cx="818" cy="300" r="143" fill="var(--marigold)"/>
      <circle cx="491" cy="686" r="214" fill="var(--teal)"/>
      <circle cx="750" cy="510" r="218" fill="var(--grape)"/>
    </g>

    <rect class="produce-top" x="98" y="0" width="697" height="108" rx="40" fill="url(#produce-top)"
          role="img" aria-label="Fresh radishes, onions, brussels sprouts and white asparagus"/>
    <circle class="stew-bowl" cx="14" cy="286" r="146" fill="url(#stew-bowl)"
            role="img" aria-label="Bowl of beef and vegetable stew"/>
    <path class="cooker-spread" d="M 60 1200 L 90 1010 Q 250 930 440 880 Q 600 860 720 940 Q 830 1000 870 1200 Z"
          fill="url(#cooker-spread)" role="img" aria-label="Stainless slow cooker surrounded by vegetables, herbs and mushrooms"/>

    <text class="author-name"><textPath href="#author-arc">Harold P. Quimby</textPath></text>
  </svg>

  <h1 class="title"><span>Hearthside</span><span>Pots</span></h1>
  <p class="tagline">Curated For Nearly Effortless Meals That Are Greater Than The Sum Of Their Ingredients</p>
</main>
</body>
</html>
```